電子書籍の表紙デザインをお願い致します。

本の内容、
冴えない20代のOLでした。そんな私でしたが約7年前に、
「たった一度きりのこの人生。もっと自分らしく、もっと輝かせたい。」
と強く熱望した瞬間があり、私は知識・人脈・実績・経験・貯金などビジネスに関してプラスになるような持ち合わせが一切ないゼロの状態で、【私らしい生き方と働き方】を一心に求めて「起業」を目指しはじめました。
今では独立を果たし、当時は未知の世界でしかなかった独立起業の道も今年で7年目に突入しました。得意な分野は、ビジネスコンサルティング、ビジネスプロデュース、コミュニティ運営、Webマーケティング、Webライティング、アフィリエイト、プロモーション、マインドコーチング、オウンドメディア構築など。写真や動画の編集・加工などクリエイティブなことも割と好きです。

私の仕事における共通点はどのビジネスでもパソコン1台とネット環境があれば場所を問わずどこでも仕事ができることです。そのライフスタイルを「スカイハーベスター」と名付け、よく国内外問わず、大好きな旅をしながら仕事をしています。

しかし、この 「起業」という働き方に出会う前の私は、好きなことをしながら仕事ができる、そんなワークスタイルがあるだなんて夢にも思っていませんでした。
そんなの理想のまた理想・・・そんなかんじで。しかしそれ以上に私が伝えたいのは、「自分でビジネスをして価値提供をする」という中で自分の思考や価値観、ライフスタイルまでも大きく変化したということなのです。そして今は毎日に充実感があり、やりがいを感じながら仕事も楽しくしています。

そして現在は、自らの経験と海外で得た感動をもとにPC1台で好きな時に・好きな場所で・好きな人と、「自分らしく、グローバルに生きていく」そんなスタイルを日々全力で、熱狂してご提供しています。

優しい雰囲気の安心できるような女性らしいカラーでお願い致します。

使って頂きたい画像と本文を添付致します。
表紙はこの4枚の画像を使って優しいイメージで、パステルカラー、薄い色を使っていただけると嬉しいです。

タイトルは
きみの毎日は花になる!扉をそっと叩いて
心ほどける日々を選び取るための小さな習慣集
でお願い致します。

はじめに、私の起業ストーリーを少しお話しさせてください。私はもともと自分に自信がまったく持てなくて、そのくせ社会不適合で、ただただ路頭に迷う、冴えない20代のOLでした。そんな私でしたが約7年前に、

日にちを19日まで延長させていただきました。
20日まで延長致しました。宜しくお願い致します。
いま、
最終段階で決定に向けて進めております。
21日で締め切らせていただきます。最後までよろしくお願いいたします。

お洒落な大人女子のイメージややんわりとしたパステルカラーの色合いがとても美しい作品だと感じました。タイトルや入れたい文字をしっかりと目立たせていただきました。自分の思い描くイメージをカタチにしてくださったなと感謝の想いでいっぱいでございます。

この度、ご提案してくださったデザイナーの皆様、最後まで吟味させて頂き、選ぶのにとても迷いました。それほど、素晴らしい作品ばかりでした。沢山のご提案を本当に有難うございました。今回はご縁を頂けなかった皆様とも、今後も定期的にコンペをさせていただく予定ですので、どうぞよろしくお願いします。

```html
<!DOCTYPE html>
<html lang="ja">
<head>
<meta charset="UTF-8">
<title>きみの毎日は花になる!扉をそっと叩いて</title>
<link href="https://fonts.googleapis.com/css2?family=Noto+Sans+JP:wght@500;800;900&family=Noto+Serif+JP:wght@500&display=swap" rel="stylesheet">
<style>
  :root {
    --paper: #ffffff;
    --ink: #2b2b2b;
    --ink-soft: #4a4a4a;
    --flower: #e8431f;
    --flower-center: #f39a2b;
    --room-top: #f3efe9;
    --room-mid: #e9e2d8;
    --room-low: #d8cfc3;
    --frame: #ffffff;
  }
  html, body {
    margin: 0;
    padding: 0;
    width: 750px;
    height: 1200px;
    overflow: hidden;
    background: var(--paper);
  }
  .cover {
    position: relative;
    width: 750px;
    height: 1200px;
    background: var(--paper);
    overflow: hidden;
    font-family: "Noto Sans JP", sans-serif;
    color: var(--ink);
  }
  .tagline-arc {
    position: absolute;
    left: 0;
    top: 0;
    width: 750px;
    height: 240px;
  }
  .tagline-arc text {
    font-family: "Noto Sans JP", sans-serif;
    font-weight: 800;
    font-size: 27px;
    letter-spacing: 4px;
    fill: var(--ink);
  }
  .title {
    position: absolute;
    left: 0;
    width: 750px;
    margin: 0;
    text-align: center;
    font-weight: 900;
    font-size: 41px;
    letter-spacing: 4px;
    line-height: 1;
    color: var(--ink);
  }
  .title--l1 { top: 245px; }
  .title--l2 { top: 312px; }
  .title--l3 { top: 378px; }
  .title--l4 { top: 468px; font-size: 42px; letter-spacing: 6px; }
  .room-scene {
    position: absolute;
    left: 0;
    top: 520px;
    width: 750px;
    height: 680px;
    background: linear-gradient(180deg, var(--room-top) 0%, #f7f4ef 35%, var(--room-mid) 62%, var(--room-low) 100%);
  }
  .photo {
    position: absolute;
    box-sizing: border-box;
    border: 6px solid var(--frame);
    box-shadow: 0 3px 10px rgba(0,0,0,0.15);
  }
  .photo--stream {
    left: 112px; top: 587px; width: 263px; height: 165px;
    background: linear-gradient(160deg, #7f9a5a 0%, #a9b98a 50%, #6f8560 100%);
  }
  .photo--rose-arch {
    left: 412px; top: 600px; width: 243px; height: 287px;
    background: linear-gradient(180deg, #d58aa3 0%, #9db67a 55%, #b8a98f 100%);
  }
  .photo--poolside {
    left: 100px; top: 795px; width: 300px; height: 267px;
    background: linear-gradient(180deg, #e6ddd0 0%, #c7d3a0 45%, #9fd0d8 80%, #e7dccb 100%);
  }
  .photo--group {
    left: 412px; top: 912px; width: 243px; height: 163px;
    background: linear-gradient(180deg, #b6a58e 0%, #d7c9b6 50%, #8d7560 100%);
  }
  .author {
    position: absolute;
    left: 500px;
    top: 1143px;
    margin: 0;
    font-family: "Noto Serif JP", serif;
    font-weight: 500;
    font-size: 19px;
    letter-spacing: 1px;
    color: var(--ink-soft);
  }
</style>
</head>
<body>
<main class="cover">
  <svg class="tagline-arc" viewBox="0 0 750 240" xmlns="http://www.w3.org/2000/svg">
    <defs>
      <path id="tagline-path" d="M 165 205 A 215 215 0 0 1 585 205"/>
    </defs>
    <text text-anchor="middle">
      <textPath href="#tagline-path" startOffset="50%">きみの毎日は花になる</textPath>
    </text>
    <g role="img" aria-label="赤いガーベラの花のイラスト">
      <circle cx="375" cy="160" r="52" fill="var(--flower)"/>
      <circle cx="375" cy="160" r="14" fill="var(--flower-center)"/>
    </g>
  </svg>

  <h1 class="title title--l1">扉をそっと叩いて</h1>
  <p class="title title--l2">心ほどける日々を</p>
  <p class="title title--l3">選び取るための</p>
  <p class="title title--l4">小さな習慣集</p>

  <div class="room-scene" role="img" aria-label="白い棚と花瓶、観葉植物のある明るい室内"></div>
  <div class="photo photo--stream" role="img" aria-label="小川のほとりで本を読む女性"></div>
  <div class="photo photo--rose-arch" role="img" aria-label="バラのアーチの下に立つ女性"></div>
  <div class="photo photo--poolside" role="img" aria-label="プールサイドのテラスでくつろぐ女性"></div>
  <div class="photo photo--group" role="img" aria-label="子どもたちとの集合写真"></div>

  <p class="author">[著] 森野ひかり</p>
</main>
</body>
</html>
```